The Brask Papers Website

I need a website to help promote the series of science fiction novels that I am in the process of writing.

I have some content and photos and am in the process of getting some new book cover artwork designed.

I have a current website/domain etc http://www.tarnwickhollow.co.nz but I need something a little more professional and eye catchig but I also want to be able to manage the content myself.

I can send e-versions of the two completed novels for context to any takers

```html
<!DOCTYPE html>
<html lang="en">
<head>
<meta charset="utf-8">
<title>The Brask Papers</title>
<link rel="stylesheet" href="https://fonts.googleapis.com/css2?family=Open+Sans:wght@400;600;700&family=Roboto:wght@100;300;400&family=Roboto+Condensed:wght@400;700&display=swap">
<style>
:root{
  --black:#000;
  --white:#fff;
  --accent:#3f97d8;
  --text:#7a7a7a;
  --dark:#222;
  --footer-bg:#fff;
  --bar-bg:#111;
  --teal-light:#46a3b3;
  --teal-mid:#1c6d80;
  --teal-dark:#0d4456;
  --field:#e4e4e4;
  --frame:#333;
  --social:#555;
  --social-first:#3b5b94;
  --fan-link:#5b7fc1;
  --like-bg:#4a67a8;
}
*{margin:0;padding:0;box-sizing:border-box}
html,body{width:868px;height:1200px;overflow:hidden;background:var(--white)}
body{font-family:"Open Sans",Arial,sans-serif;color:var(--text)}
.canvas{position:relative;width:868px;height:1200px;overflow:hidden}

/* header */
.site-header{position:absolute;left:0;top:0;width:868px;height:55px;background:var(--black)}
.logo{position:absolute;left:56px;top:11px;font-family:"Roboto Condensed",Arial,sans-serif;font-weight:700;font-size:26px;color:var(--white)}
.main-nav{position:absolute;right:24px;top:17px;display:flex}
.main-nav a{font-size:15.5px;color:var(--white);text-decoration:none;margin-left:28px}
.main-nav a.is-active{color:var(--accent)}

/* hero */
.hero{position:absolute;left:0;top:55px;width:868px;height:382px;
  background:radial-gradient(ellipse 520px 330px at 430px 40px,var(--teal-light),var(--teal-mid) 55%,var(--teal-dark));overflow:hidden}
.hero-title{position:absolute;left:130px;top:78px;color:var(--white);line-height:1;font-weight:400}
.hero-title .series{display:block;font-family:"Roboto",Arial,sans-serif;font-weight:100;font-size:100px;letter-spacing:4px;line-height:96px}
.hero-title .line{display:block;font-family:"Roboto Condensed",Arial,sans-serif;font-weight:400;font-size:66px;line-height:66px}
.hero-title .line.bold{font-weight:700}
.hero-title .author{display:block;font-family:"Roboto",Arial,sans-serif;font-weight:300;font-size:32px;letter-spacing:2px;margin-top:4px}
.hero-cover{position:absolute;left:502px;top:6px;width:210px;height:350px;
  background:linear-gradient(180deg,#1a1a1a 0%,#8d8d8d 25%,#6a6a6a 60%,#f2f2f2 62%,#ffffff 100%);
  box-shadow:10px 10px 20px rgba(0,0,0,.35)}
.hero-arrow{position:absolute;top:165px}

/* buy bar */
.buy-bar{position:absolute;left:0;top:437px;width:868px;height:42px;background:var(--black)}
.buy-label{position:absolute;left:56px;top:10px;font-size:16px;color:var(--white);font-weight:600}
.retailer{position:absolute;top:11px;height:20px;background:var(--white);font-size:9px;font-weight:700;color:var(--dark);text-align:center;line-height:20px;white-space:nowrap}

/* about */
.about-title{position:absolute;left:56px;top:497px;font-size:15.5px;font-weight:600;color:var(--dark)}
.author-photo{position:absolute;left:56px;top:523px;width:142px;height:175px;background:linear-gradient(160deg,#9fb9c6,#d8c7b4 55%,#5c5c66)}
.about-text{position:absolute;left:212px;top:516px;width:374px;font-size:10.4px;line-height:15.5px}
.about-text p{margin-bottom:6px}
.btn{display:block;background:var(--accent);color:var(--white);text-align:center;font-size:10px}
.read-more{position:absolute;left:523px;top:677px;width:60px;height:20px;line-height:20px}

.sidebar{position:absolute;left:606px;top:502px;width:206px;height:196px;background:var(--black);color:var(--white);padding:10px 14px}
.sidebar h3{font-size:15px;font-weight:600}
.sidebar .hint{font-size:10.5px;font-weight:600;margin-top:1px}
.field{margin-top:7px;width:176px;height:22px;background:var(--field);color:#999;font-size:9px;line-height:22px;padding-left:6px}
.signup{margin-top:10px;width:50px;height:19px;line-height:19px;font-size:9.5px}
.sidebar h3.find{margin-top:11px}
.fan-photo{position:absolute;left:14px;top:141px;width:40px;height:40px;background:linear-gradient(160deg,#8fa9b6,#c9b7a3 60%,#555)}
.fan-name{position:absolute;left:62px;top:141px;font-size:11.5px;color:var(--fan-link)}
.like{position:absolute;left:62px;top:160px;width:36px;height:14px;background:var(--like-bg);font-size:8.5px;font-weight:700;color:var(--white);line-height:14px;padding-left:4px}
.like-count{position:absolute;left:104px;top:161px;font-size:9px;color:#999}

/* books */
.books{position:absolute;left:0;top:721px;width:868px;height:285px;background:var(--black)}
.books h2{position:absolute;left:56px;top:19px;font-size:15.5px;font-weight:600;color:var(--white)}
.book{position:absolute;top:43px;width:159px}
.book-cover{height:185px;border:1px solid var(--frame);padding:4px}
.book-cover .art{width:100%;height:100%}
.book.is-selected .book-cover{border:2px solid var(--accent)}
.book-link{margin-top:5px;height:31px;border:1px solid var(--frame);color:var(--white);font-size:13px;text-align:center;line-height:29px}
.book.is-selected .book-link{background:var(--accent);border-color:#8cc3ec}
.books-arrow{position:absolute;top:130px}

/* footer */
.site-footer{position:absolute;left:0;top:1006px;width:868px;height:156px;background:var(--footer-bg)}
.footer-col{position:absolute;top:18px}
.footer-col h4{font-size:15.5px;font-weight:600;color:var(--dark);margin-bottom:5px}
.footer-col li{list-style:none;font-size:10.2px;line-height:19.6px;color:var(--text)}
.footer-col li.is-current{color:var(--accent)}
.footer-col.news li{font-weight:600}
.contact-row{position:absolute;left:19px;font-size:10.2px;line-height:15px;width:190px}
.contact-icon{position:absolute;left:0}

.bottom-bar{position:absolute;left:0;top:1162px;width:868px;height:38px;background:var(--bar-bg)}
.copyright{position:absolute;left:56px;top:12px;font-size:10px;color:#8a8a8a}
.social{position:absolute;top:9px;width:19px;height:19px;background:var(--social)}
.social.first{background:var(--social-first)}
</style>
</head>
<body>
<div class="canvas">

  <header class="site-header">
    <div class="logo">The Brask Papers</div>
    <nav class="main-nav">
      <a class="is-active">Home</a><a>Reviews</a><a>About</a><a>Blog</a><a>Contact</a><a>Links</a>
    </nav>
  </header>

  <section class="hero">
    <svg class="hero-arrow" style="left:68px" width="24" height="70" viewBox="0 0 24 70"><polyline points="20,2 4,35 20,68" fill="none" stroke="#fff" stroke-width="2.5"/></svg>
    <h1 class="hero-title">
      <span class="series">BRASK</span>
      <span class="line">THE FIRST</span>
      <span class="line bold">PAPER</span>
      <span class="author">ORRIN TALVEY</span>
    </h1>
    <div class="hero-cover" role="img" aria-label="Book cover of Brask: The First Paper, a photograph of the moon above a white title panel"></div>
    <svg class="hero-arrow" style="left:776px" width="24" height="70" viewBox="0 0 24 70"><polyline points="4,2 20,35 4,68" fill="none" stroke="#fff" stroke-width="2.5"/></svg>
  </section>

  <div class="buy-bar">
    <div class="buy-label">Buy Now</div>
    <div class="retailer" style="left:135px;width:66px">Shelfway</div>
    <div class="retailer" style="left:217px;width:72px">Quill &amp; Lane</div>
    <div class="retailer" style="left:305px;width:62px">Bookmarket</div>
    <div class="retailer" style="left:381px;width:80px">Pressgrove</div>
    <div class="retailer" style="left:475px;width:63px">Pagely</div>
  </div>

  <section class="about">
    <h2 class="about-title">Meet Orrin Talvey</h2>
    <div class="author-photo" role="img" aria-label="Portrait photograph of the author Orrin Talvey seated outdoors"></div>
    <div class="about-text">
      <p>For as long as he can remember Orrin has wanted to be a writer and he has taken a long and sometime torturous path towards being published on Shelfway. The advent of Shelfway's simple and effective self publishing tools has allowed him to finally realize this dream.</p>
      <p>Orrin has had had jobs that range from being a shepherd to a courier in Central Auckland, New Zealand. In between he has also found time to ride a dirtbike (slowly now) and play with video cameras.</p>
      <p>Sci-fi is Orrin's first love, whether it be reading or writing it. While he has a full time job in the transport industry that pays the bills, Orrin still finds time to put his image in ation to work.</p>
    </div>
    <a class="btn read-more">Read More</a>

    <aside class="sidebar">
      <h3>MAILING LIST</h3>
      <div class="hint">Sign up for email updates:</div>
      <div class="field">Enter your Name address</div>
      <a class="btn signup">SIGN UP</a>
      <h3 class="find">Find Orrin Online</h3>
      <div class="fan-photo" role="img" aria-label="Small profile photograph of Orrin Talvey"></div>
      <div class="fan-name">Orrin Talvey</div>
      <div class="like">Like</div>
      <div class="like-count">1205 Peole like</div>
    </aside>
  </section>

  <section class="books">
    <h2>My Books</h2>
    <svg class="books-arrow" style="left:66px" width="16" height="26" viewBox="0 0 16 26"><polyline points="13,2 3,13 13,24" fill="none" stroke="#fff" stroke-width="3.5"/></svg>
    <div class="book is-selected" style="left:94px">
      <div class="book-cover"><div class="art" role="img" aria-label="Cover of The Second Drift, the second Brask novel, a silver spacecraft over a red title band" style="background:linear-gradient(180deg,#111 0%,#8a8a8a 35%,#3a3a3a 58%,#e1100f 60%,#e1100f 100%)"></div></div>
      <div class="book-link">Click to Leran More</div>
    </div>
    <div class="book" style="left:267px">
      <div class="book-cover"><div class="art" role="img" aria-label="Cover of Brushwork Basics, a painted waterfall landscape" style="background:linear-gradient(180deg,#f1ecd6 0%,#e9e2c4 35%,#9bb270 60%,#6d8b58 80%,#c7c5b3 100%)"></div></div>
      <div class="book-link">Click to Leran More</div>
    </div>
    <div class="book" style="left:441px">
      <div class="book-cover"><div class="art" role="img" aria-label="Cover of Weather, Tone and Glow, a painted mountain landscape" style="background:linear-gradient(180deg,#ecedf0 0%,#d7dbe6 40%,#a9a6b5 62%,#c9b68d 85%,#e8e4d2 100%)"></div></div>
      <div class="book-link">Click to Leran More</div>
    </div>
    <div class="book" style="left:614px">
      <div class="book-cover"><div class="art" role="img" aria-label="Cover of The Northern Line Story, a tinted photograph of a steam locomotive" style="background:linear-gradient(180deg,#2f6f7a 0%,#1d4e58 50%,#8a4a1f 70%,#5a2a12 100%)"></div></div>
      <div class="book-link">Click to Leran More</div>
    </div>
    <svg class="books-arrow" style="left:786px" width="16" height="26" viewBox="0 0 16 26"><polyline points="3,2 13,13 3,24" fill="none" stroke="#fff" stroke-width="3.5"/></svg>
  </section>

  <footer class="site-footer">
    <div class="footer-col" style="left:56px">
      <h4>The Website</h4>
      <ul><li class="is-current">Home Page</li><li>Contact Information</li><li>Orrin Talvey Biography</li><li>Interview with Orrin Talvey</li><li>Frequently Asked Questions</li></ul>
    </div>
    <div class="footer-col" style="left:274px">
      <h4>The Book</h4>
      <ul><li>Novel</li><li>Comdey</li><li>Darma</li><li>Social</li><li>Polictical</li></ul>
    </div>
    <div class="footer-col news" style="left:422px">
      <h4>The News</h4>
      <ul><li>Recent News</li><li>Orrin Talvey's Blog</li><li>Follow Orrin on Chirper</li><li>Upcoming Events</li></ul>
    </div>
    <div class="footer-col" style="left:619px;width:200px;height:130px">
      <h4>Contact</h4>
      <div class="contact-row" style="top:24px">Orrin Talvey PO Box 40718<br>Auckland<br>New Zealand</div>
      <svg class="contact-icon" style="top:25px" width="14" height="16" viewBox="0 0 14 16"><path d="M7 1a4.5 4.5 0 0 0-4.5 4.5C2.5 9 7 13 7 13s4.5-4 4.5-7.5A4.5 4.5 0 0 0 7 1z" fill="none" stroke="#3f97d8" stroke-width="1.3"/><circle cx="7" cy="5.5" r="1.5" fill="#3f97d8"/><path d="M1 15h12" stroke="#3f97d8" stroke-width="1.3"/></svg>
      <div class="contact-row" style="top:79px">Phone: +0272 555 014</div>
      <svg class="contact-icon" style="top:78px" width="10" height="16" viewBox="0 0 10 16"><path d="M3 1h2l1 4-2 1c0 2 1 4 2 5l2-1 1 4-2 1C3 14 1 9 1 4z" fill="#3f97d8"/></svg>
      <div class="contact-row" style="top:104px">Email: orrin@tarnwickhollow.co.nz</div>
      <svg class="contact-icon" style="top:106px" width="14" height="10" viewBox="0 0 14 10"><rect x="0.7" y="0.7" width="12.6" height="8.6" fill="none" stroke="#3f97d8" stroke-width="1.2"/><polyline points="1,1 7,6 13,1" fill="none" stroke="#3f97d8" stroke-width="1.2"/></svg>
    </div>
  </footer>

  <div class="bottom-bar">
    <div class="copyright">Copyright &copy; 2014 The Brask Papers . All Rights Reserved.</div>
    <div class="social first" style="left:656px"></div>
    <div class="social" style="left:679px"></div>
    <div class="social" style="left:702px"></div>
    <div class="social" style="left:725px"></div>
    <div class="social" style="left:748px"></div>
    <div class="social" style="left:771px"></div>
    <div class="social" style="left:793px"></div>
  </div>

</div>
</body>
</html>
```